Business Card Design Project

I want a cleaner business card and envelope then what we have now, its too crowded.
Updates

I update with logo, this can be changed anyway you feel it looks best. I also have put gaurantee on there and extended time, this is my first time doing this. Also gave an example of current card

Target Market(s)

a wide array of customers from vantage 400 to small companies and cleints

Industry/Entity Type

Business

Requirements
Must have
• Need to have address, telephone number email
Nice to have
• a sharp professional card that stands out but is still very clean.
Should not have
• Not crazy looking

```html
<!DOCTYPE html>
<html lang="en">
<head>
<meta charset="utf-8">
<title>Harborline Insurance Group – Business Card</title>
<link rel="stylesheet" href="https://fonts.googleapis.com/css2?family=Jost:wght@400;500&display=swap">
<style>
  :root {
    --yellow: #f9c22e;
    --yellow-panel: #f8c12b;
    --fold-top: #e4bd58;
    --fold-left: #dfb12f;
    --fold-right: #fbd97c;
    --fold-bottom: #fbcf4f;
    --fold-edge: #c79a22;
    --tab: #414042;
    --ink: #231f20;
    --trim: #bfe3e6;
    --page: #ffffff;
  }
  * { box-sizing: border-box; margin: 0; padding: 0; }
  html, body { width: 985px; height: 1200px; overflow: hidden; background: var(--page); }
  body { position: relative; font-family: "Jost", "Futura", sans-serif; color: var(--ink); }

  .card {
    position: absolute;
    left: 36px;
    width: 909px;
    height: 521px;
    background: var(--yellow);
    outline: 1px solid var(--trim);
    overflow: hidden;
  }
  .card--front { top: 38px; }
  .card--back { top: 608px; }

  .card__folds { position: absolute; inset: 0; width: 100%; height: 100%; }

  .tab {
    position: absolute;
    width: 26px;
    background: var(--tab);
  }
  .card--front .tab { top: 64px; height: 386px; }
  .card--back .tab { top: 71px; height: 386px; }
  .tab--left { left: 0; border-radius: 0 13px 13px 0; }
  .tab--right { right: 0; border-radius: 13px 0 0 13px; }

  .brand {
    position: absolute;
    left: 194px; top: 90px;
    width: 520px; height: 340px;
    display: flex; flex-direction: column; align-items: center; justify-content: center;
  }
  .brand__mark {
    width: 150px; height: 150px;
    background: #9a9a9c;
    margin-bottom: 26px;
  }
  .brand__name {
    font-weight: 500;
    font-size: 52px;
    letter-spacing: 5px;
    line-height: 1;
    text-transform: uppercase;
  }
  .brand__tagline {
    font-weight: 500;
    font-size: 25px;
    letter-spacing: 4px;
    margin-top: 10px;
    text-transform: uppercase;
  }
  .front__web {
    position: absolute;
    left: 0; right: 0; top: 470px;
    text-align: center;
    font-size: 22px;
  }

  .contact {
    position: absolute;
    left: 88px; top: 114px;
    font-size: 20px;
    line-height: 26px;
  }
  .contact__name { font-size: 25px; line-height: 30px; }
  .contact__role { font-size: 19px; line-height: 24px; margin-bottom: 20px; }
  .contact__block + .contact__block { margin-top: 26px; }

  .services {
    position: absolute;
    left: 540px; top: 33px;
    font-size: 20px;
    line-height: 26px;
  }
  .services__group + .services__group { margin-top: 20px; }
  .services__title { text-transform: uppercase; }
  .services__list { list-style: none; }
  .services__list li { padding-left: 13px; text-indent: -13px; }
  .services__list li::before { content: "•"; margin-right: 5px; }
</style>
</head>
<body>

<section class="card card--front" aria-label="Card front">
  <svg class="card__folds" viewBox="0 0 909 521" aria-hidden="true">
    <polygon points="0,0 909,0 714,90 194,90" fill="var(--fold-top)"/>
    <polygon points="0,0 194,90 194,430 0,521" fill="var(--fold-left)"/>
    <polygon points="909,0 714,90 714,430 909,521" fill="var(--fold-right)"/>
    <polygon points="0,521 194,430 714,430 909,521" fill="var(--fold-bottom)"/>
    <line x1="909" y1="0" x2="714" y2="90" stroke="var(--fold-edge)" stroke-width="8"/>
    <line x1="0" y1="521" x2="194" y2="430" stroke="var(--fold-edge)" stroke-width="8"/>
    <rect x="194" y="90" width="520" height="340" fill="var(--yellow-panel)"/>
  </svg>
  <div class="tab tab--left"></div>
  <div class="tab tab--right"></div>

  <div class="brand">
    <div class="brand__mark"></div>
    <div class="brand__name">Harborline</div>
    <div class="brand__tagline">Insurance Group</div>
  </div>
  <p class="front__web">www.harborlineagency.com</p>
</section>

<section class="card card--back" aria-label="Card back">
  <div class="tab tab--left"></div>
  <div class="tab tab--right"></div>

  <div class="contact">
    <p class="contact__name">Claire Whitmore-Dane</p>
    <p class="contact__role">Operations Manager</p>
    <div class="contact__block">
      <p>Phone: 555-410-2600 ext 118</p>
      <p>Direct: 555-410-7724</p>
      <p>Fax: 555-410-2609</p>
      <p>cwhitmore-dane@harborlineagency.com</p>
    </div>
    <div class="contact__block">
      <p>18230 Maple Crest Ave.</p>
      <p>Lakeview Park, MI 48990</p>
      <p>www.harborlineagency.com</p>
    </div>
  </div>

  <div class="services">
    <div class="services__group">
      <p class="services__title">Commercial Insurance</p>
      <ul class="services__list">
        <li>Traditional Insurance</li>
        <li>Coverage</li>
        <li>Executive Protection Coverage</li>
        <li>Speciality Coverage Insurance</li>
      </ul>
    </div>
    <div class="services__group">
      <p class="services__title">Personal Insurance</p>
      <ul class="services__list">
        <li>Auto/Recreational/Boat</li>
        <li>Home/Renters/Condo</li>
        <li>Umbrella Liability</li>
      </ul>
    </div>
    <div class="services__group">
      <p class="services__title">Employee Benefits</p>
      <ul class="services__list">
        <li>Medical/Dental/Optical Plans</li>
        <li>Prescription Coverage</li>
        <li>Life &amp; Accidental Death &amp;<br>Dismemberment Insurance</li>
        <li>Disability Insurance</li>
        <li>Voluntary Benefits</li>
      </ul>
    </div>
  </div>
</section>

</body>
</html>
```